Pricing Page; Request Quote Page Design

I'm looking to update our pricing page and request page to something more modern in terms of the layout/form design and with more content, but needs to be consistent with the rest of our site. I need two pages designed. 1) A general pricing page w/ CTAs for quotes, and 2) The request quote page with form. Ideally there would be (3) parts for our different packages (Express, Professional, Enterprise) on the pricing page, with CTAs on each section. I like the hero image approach used here https://quillrift.com/pricing and here http://www.morvashelf.com/wp-content/uploads/2016/08/tandorix-pricing-page-design.png In terms of the form page, mainly just looking for an improvement over this https://www.pelwickstudios.com/price-quote-request

I also included a sample mockup to provide a BIT of guidance, but looking for something a little different and modern.

Industry/Entity Type

Pricing

Number of Pages Required

2 page

Font styles to use
Sans Serif

Requirements
Must have
• Hero background image on main pricing page. Needs to follow the look and feel of pelwickstudios.com

```html
<!DOCTYPE html>
<html lang="en">
<head>
<meta charset="utf-8">
<title>Pricing — Pelwick Studios</title>
<link href="https://fonts.googleapis.com/css2?family=Raleway:wght@300;400;500;600;700&display=swap" rel="stylesheet">
<style>
:root{
  --ink:#2b2b2b;
  --card-head:#262626;
  --footer:#1b1b1b;
  --green:#99cc00;
  --green-text:#8cbf1f;
  --text:#555;
  --paper:#f6f6f6;
  --line:#e2e2e2;
  --white:#fff;
}
*{margin:0;padding:0;box-sizing:border-box}
html,body{width:1093px;height:1200px;overflow:hidden}
body{font-family:'Raleway',sans-serif;background:var(--paper);position:relative;color:var(--text)}
.topbar{position:absolute;left:0;top:0;width:1093px;height:104px;background:var(--ink)}
.call{position:absolute;left:709px;top:18px;color:var(--green-text);font-weight:700;font-size:14px;letter-spacing:.5px}
.demo-btn{position:absolute;left:894px;top:11px;width:120px;height:32px;background:#76a51f;color:var(--white);font-size:11.5px;font-weight:700;display:flex;align-items:center;justify-content:center;letter-spacing:.3px}
.brand{position:absolute;left:78px;top:74px;display:flex;align-items:center;gap:7px;font-size:14px;font-weight:600;color:var(--white)}
.brand .mark{width:11px;height:11px;background:var(--white)}
.nav{position:absolute;right:79px;top:76px;display:flex;gap:22px;list-style:none}
.nav li{color:var(--white);font-size:14.5px;font-weight:500;letter-spacing:.3px}
.hero{position:absolute;left:0;top:104px;width:1093px;height:480px;
  background:
    radial-gradient(ellipse 260px 200px at 120px 120px,rgba(214,220,212,.9),transparent 70%),
    radial-gradient(ellipse 300px 260px at 560px 140px,rgba(200,198,196,.75),transparent 70%),
    radial-gradient(ellipse 280px 170px at 520px 440px,rgba(176,158,140,.65),transparent 70%),
    radial-gradient(ellipse 260px 320px at 960px 300px,rgba(22,26,34,.9),transparent 70%),
    linear-gradient(100deg,#8d948e 0%,#a6a9a4 30%,#8c8580 52%,#4d4f55 75%,#24272e 100%)}
.hero-shade{position:absolute;inset:0;background:rgba(20,20,25,.3)}
.hero h1{position:absolute;left:0;width:100%;top:308px;margin-top:-104px;text-align:center;color:var(--white);font-weight:300;font-size:39px;letter-spacing:.8px}
.hero p{position:absolute;left:150px;width:793px;top:280px;text-align:center;color:var(--white);font-size:14.2px;line-height:24px;letter-spacing:.4px;text-transform:uppercase;font-weight:400}
.plans{position:absolute;left:0;top:584px;width:1093px;height:536px;background:var(--paper)}
.plan{position:absolute;background:var(--white);border:1px solid var(--line);top:53px;width:298px;height:457px}
.plan-head{height:120px;background:var(--card-head);color:var(--white);display:flex;align-items:center;justify-content:center;font-size:36px;font-weight:600;letter-spacing:2px}
.plan p{text-align:center;font-size:19px;line-height:29px;padding:34px 6px 0;letter-spacing:.5px;font-weight:400}
.quote-btn{position:absolute;left:15px;right:15px;bottom:22px;height:59px;border:2px solid var(--line);display:flex;align-items:center;justify-content:center;font-size:24px;letter-spacing:1px;color:var(--text)}
.plan.express{left:102px}
.plan.enterprise{left:697px}
.plan.featured{left:399px;top:29px;height:481px;border-top:none}
.plan.featured .plan-head{height:144px;background:var(--green);padding-bottom:24px}
.plan.featured .quote-btn{background:var(--green);border-color:var(--green);color:var(--white);left:16px;right:16px}
.footer{position:absolute;left:0;top:1120px;width:1093px;height:80px;background:var(--footer)}
.footer-links{position:absolute;left:79px;top:15px;width:560px;display:flex;flex-wrap:wrap;column-gap:22px;list-style:none;line-height:19px}
.footer-links li{color:var(--white);font-size:15px;font-weight:500}
.legal{position:absolute;left:720px;top:26px;font-size:8.5px;color:#bbb}
.legal a{color:var(--green);text-decoration:none}
.help{position:absolute;left:966px;top:17px;width:48px;height:48px;background:var(--green);display:flex;align-items:center;justify-content:center}
</style>
</head>
<body>
<header class="topbar">
  <div class="call">CALL 1-866-555-0142</div>
  <div class="demo-btn">REQUEST DEMO</div>
  <div class="brand"><span class="mark"></span><span>Pelwick Studios</span></div>
  <ul class="nav">
    <li>FEATURES</li><li>SERVICES</li><li>PRICING</li><li>RESSOURCES</li><li>BLOG</li><li>NEWS</li><li>CONTACT</li>
  </ul>
</header>

<section class="hero">
  <div class="hero-shade" role="img" aria-label="Photo of a business team meeting around a bright office table"></div>
  <h1>Flexible Pricing Designed to Fit Your Business</h1>
  <p>Our pay-as-you-grow pricing model is geared to minimize risk and maximize return. Whether launching a new learning initiative, or looking to migrate (or integrate) an existing business with our learning business platform, we have you covered.</p>
</section>

<section class="plans">
  <div class="plan express">
    <div class="plan-head">Express</div>
    <p>Launch in weeks, not months. Perfect for smaller businesses with less than 1,000 users and requiring less than 25 courses. Packages start at $499.</p>
    <div class="quote-btn">Request Quote</div>
  </div>
  <div class="plan featured">
    <div class="plan-head">Professional</div>
    <p>Designed for more established learning businesses which are need to scale and leverage modern technology. Up to 10k users &amp; 100 courses..</p>
    <div class="quote-btn">Request Quote</div>
  </div>
  <div class="plan enterprise">
    <div class="plan-head">Entreprise</div>
    <p>For larger organizations needing to scale learning globally to more than 10,000 users, with hundreds of courses and multiple instances.</p>
    <div class="quote-btn">Request Quote</div>
  </div>
</section>

<footer class="footer">
  <ul class="footer-links">
    <li>Features</li><li>Services</li><li>Picing</li><li>Ressources</li><li>Bog</li><li>News</li><li>Carrers</li><li>Contact</li>
  </ul>
  <div class="legal">Copyright © 2016 Pelwick Studios,Inc &nbsp;|&nbsp; <a href="#">Privacy policy</a></div>
  <div class="help">
    <svg width="26" height="24" viewBox="0 0 26 24" fill="none" stroke="#fff" stroke-width="1.4">
      <rect x="8" y="2" width="16" height="12" rx="2"/>
      <path d="M6 8H3a1.5 1.5 0 0 0-1.5 1.5v7A1.5 1.5 0 0 0 3 18h2v4l4-4h6a1.5 1.5 0 0 0 1.5-1.5V14"/>
      <path d="M14 6.5a2 2 0 1 1 2.5 1.9c-.4.2-.5.5-.5.9v.7"/>
      <circle cx="16" cy="11.6" r=".5" fill="#fff"/>
    </svg>
  </div>
</footer>
</body>
</html>
```